Need Two Flyers Created

I need two flyers created:
(1) Marketing me as a speaker with an upcoming book coming out including past topics I've spoken on with contact information - a pic of me will be included as well as a pic of the book; and
(2) marketing my new company - The Korvell Partners, Inc., and our four pillars: Leadership Development, School Improvement, Superintendent/Central Office Support, and Strategic Advisory Services.

Target Market(s)

Educators
Business Leaders
Organization Leaders
Leaders in general

Industry/Entity Type

Marketing

Requirements
Must have
• Very creative but not overwhelming
• A picture of me
• A picture of the front of the book.

```html
<!DOCTYPE html>
<html lang="en">
<head>
<meta charset="utf-8">
<title>M. Rowan Hale — Purposeful Excellence</title>
<link href="https://fonts.googleapis.com/css2?family=Oswald:wght@300;400;500;600;700&family=Montserrat:wght@400;500;800;900&display=swap" rel="stylesheet">
<style>
  :root{
    --navy:#0d3f7a;
    --blue:#1e5b98;
    --bright:#2a8be0;
    --ink:#3d3d3d;
    --paper:#f4f4f4;
    --mist:#dcdcdc;
    --crimson:#c8234a;
    --gold:#f3d04a;
    --steel-top:#ffffff;
    --steel-mid:#b9bec4;
    --steel-low:#e9ecef;
  }
  *{box-sizing:border-box;margin:0;padding:0}
  html,body{width:1155px;height:1200px;overflow:hidden;background:#ffffff}
  .flyer{position:relative;width:1155px;height:1200px;overflow:hidden;
    background:linear-gradient(180deg,#ffffff 0%,var(--paper) 45%,#e6e6e6 75%,#dadada 100%);
    font-family:"Oswald",sans-serif}
  .pattern-zone{position:absolute;left:0;top:0;width:220px;height:560px;
    background:linear-gradient(135deg,#d9d9d9 0%,#ececec 45%,rgba(255,255,255,0) 100%)}
  .portrait{position:absolute;left:740px;top:15px;width:415px;height:560px;
    background:radial-gradient(ellipse at 50% 35%,#9a9a9a 0%,#bdbdbd 40%,#dedede 70%,rgba(240,240,240,0) 100%)}
  .speaker-name{position:absolute;left:130px;top:62px;font-weight:600;font-size:64px;
    letter-spacing:-0.5px;color:var(--blue);line-height:1}
  .speaker-name .degree{font-size:30px;font-weight:500}
  .name-rule{position:absolute;left:130px;top:138px;width:614px;height:1px;background:#9a9a9a}
  .tagline{position:absolute;left:130px;top:146px;width:620px;font-weight:300;font-size:20.5px;
    color:var(--ink);line-height:25px}

  .book-stack{position:absolute;left:610px;top:560px;width:510px;height:300px;
    background:linear-gradient(180deg,#e9e9e9 0%,#f7f7f7 50%,#cfcfcf 100%)}
  .book-cover{position:absolute;left:70px;top:255px;width:575px;height:570px;background:#ffffff;
    box-shadow:0 10px 24px rgba(0,0,0,.25);overflow:hidden}
  .cover-photo{position:absolute;left:0;top:0;width:100%;height:235px;
    background:linear-gradient(180deg,#c9a37f 0%,#a57547 60%,#8a5a31 100%)}
  .cover-band{position:absolute;left:0;top:225px;width:100%;height:92px;background:var(--crimson)}
  .cover-title{position:absolute;left:0;width:100%;top:180px;text-align:center;font-family:"Oswald",sans-serif;
    font-weight:500;font-style:italic;font-size:82px;color:#ffffff;letter-spacing:-1px;line-height:1}
  .cover-sub{position:absolute;left:0;width:100%;top:268px;text-align:center;font-family:"Montserrat",sans-serif;
    font-weight:500;font-size:32px;letter-spacing:9px;color:var(--gold)}
  .cover-number{position:absolute;left:120px;top:345px;width:82px;height:82px;border-radius:50%;
    background:#2d6a96;color:#ffffff;font-family:"Oswald",sans-serif;font-style:italic;font-size:56px;
    text-align:center;line-height:82px}
  .cover-strategy{position:absolute;left:220px;top:350px;font-family:"Montserrat",sans-serif;font-size:13.5px;
    letter-spacing:2px;line-height:19px;color:#555;text-transform:uppercase}
  .cover-author{position:absolute;left:0;width:100%;top:475px;text-align:center;font-family:"Oswald",sans-serif;
    font-style:italic;font-size:44px;color:var(--crimson)}
  .cover-foreword{position:absolute;left:0;width:100%;top:532px;text-align:center;font-family:"Montserrat",sans-serif;
    font-size:13px;letter-spacing:2px;color:#666;text-transform:uppercase}

  .wave{position:absolute;left:0;top:820px;width:1155px;height:380px}

  .steel{background:linear-gradient(180deg,var(--steel-top) 0%,var(--steel-low) 45%,var(--steel-mid) 55%,#f4f5f6 100%);
    -webkit-background-clip:text;background-clip:text;color:transparent}
  .release-month{position:absolute;left:40px;top:1163px;transform-origin:0 0;transform:rotate(-90deg);
    font-weight:600;font-size:60px;line-height:1;letter-spacing:0}
  .release-word{position:absolute;left:128px;top:975px;font-weight:700;font-size:98px;line-height:1;letter-spacing:-1px}
  .release-year{position:absolute;left:128px;top:1062px;font-family:"Montserrat",sans-serif;font-weight:900;
    font-size:110px;line-height:1;letter-spacing:-2px}
  .divider{position:absolute;left:545px;top:985px;width:1px;height:170px;background:rgba(255,255,255,.45)}
  .contact-line{position:absolute;left:573px;top:975px;font-weight:500;font-size:33px;line-height:1;letter-spacing:-0.3px}
  .bookings{position:absolute;left:573px;top:1010px;font-weight:700;font-size:84px;line-height:1;letter-spacing:0}
  .company-name{position:absolute;left:573px;top:1118px;width:230px;font-weight:400;font-size:22px;line-height:26px;color:#ffffff}
  .web-dot{position:absolute;left:936px;top:1114px;width:14px;height:14px;border-radius:50%;background:#ffffff}
  .website{position:absolute;left:826px;top:1133px;width:235px;text-align:center;font-family:"Montserrat",sans-serif;
    font-weight:800;font-size:15px;color:#ffffff}
</style>
</head>
<body>
<div class="flyer">
  <div class="pattern-zone" role="img" aria-label="Soft grey geometric backdrop in the top left corner"></div>
  <div class="portrait" role="img" aria-label="Black and white portrait of the speaker in a suit"></div>

  <h1 class="speaker-name">M. ROWAN HALE,<span class="degree"> Ph.D.</span></h1>
  <div class="name-rule"></div>
  <p class="tagline">Father, Leader, Educator, Author &amp; Innovator Reasonably impatient about improving educational outcomes for ALL children</p>

  <div class="book-stack" role="img" aria-label="Stack of three copies of the book seen from the spine"></div>

  <div class="book-cover">
    <div class="cover-photo" role="img" aria-label="Classroom photo of students talking with the author at a table"></div>
    <div class="cover-band"></div>
    <div class="cover-title">PURPOSEFUL</div>
    <div class="cover-sub">EXCELLENCE</div>
    <div class="cover-number">3</div>
    <div class="cover-strategy">Fundamental<br>strategies that<br>drive educational<br>leadership</div>
    <div class="cover-author">M. Rowan Hale</div>
    <div class="cover-foreword">Foreword by Lionel Marsh</div>
  </div>

  <svg class="wave" viewBox="0 0 1155 380" preserveAspectRatio="none" aria-hidden="true">
    <defs>
      <linearGradient id="deep" x1="0" y1="0" x2="0" y2="1">
        <stop offset="0" stop-color="#1b5ea8"/>
        <stop offset="1" stop-color="#0b3a72"/>
      </linearGradient>
    </defs>
    <path d="M0 30 C300 60 600 100 1155 40 L1155 380 L0 380 Z" fill="#bfc3c8"/>
    <path d="M0 40 C300 75 650 120 1155 55 L1155 380 L0 380 Z" fill="#1a62b0"/>
    <path d="M0 55 C300 95 650 135 1155 70 L1155 380 L0 380 Z" fill="#2a8be0"/>
    <path d="M0 70 C320 120 700 140 1155 80 L1155 380 L0 380 Z" fill="#ffffff"/>
    <path d="M0 85 C340 135 720 150 1155 92 L1155 380 L0 380 Z" fill="#3a9be8"/>
    <path d="M0 100 C360 140 760 130 1155 100 L1155 380 L0 380 Z" fill="url(#deep)"/>
  </svg>

  <div class="release-month steel">JANUARY</div>
  <div class="release-word steel">RELEASED</div>
  <div class="release-year steel">2018</div>
  <div class="divider"></div>
  <div class="contact-line steel">Contact info@korvellpartners.com</div>
  <div class="bookings steel">FOR BOOKINGS</div>
  <div class="company-name">The Korvell Partners, Inc.</div>
  <div class="web-dot"></div>
  <div class="website">www.korvellpartners.com</div>
</div>
</body>
</html>
```